Advertising Portal Needs eBrochure

Hi Crowders! Our advertising portal, which focus on the new launches property, needs an online brochure to promote to potential advertisers the benefits of advertising their projects with us. These advertisers will be mainly real estate developers and agencies.

WHAT WE LOOKING FOR
We do not want over-fanciful designs that makes the content hard to read. The use of illustrations and graphics/symbols related to covered topics are encouraged. The overall design should portrait our advertising efficiency through online and social media means. Our website - www.brightkeyhomes.sg.

For draft purposes, just do up the front page, back page, and few inner pages, preferably to include one illustration chart (either on page 7/8). Size wise probably A5 portrait or landscape, for future printing into a booklet.

WORK COMPLETION AND PAYMENT
The $500 stated here is 50% of the payment. Upon getting a desired draft design, we will need you to work on the full content with slight amendments along the way. Once done, we will be paying the balance $500, and we will need the pdf file as well as the work file.

Let your design juice flow, and hope we can work with you!

Hi Crowders! Thank you for your submissions. We are closing the project as we've decided on a design. It's a pity we can only select one design, as there are a number of good works. Hope we will have a chance to work together on our upcoming projects. Cheers =)

Target Market(s)

Real estate developers, real estate agencies, and perhaps to an extent, individual property sales agent.

Industry/Entity Type

Advertising

Requirements
Should not have
• We prefer not to have much real people kind of stock images. Try not to use images from our portal as we do not have the ownerships. Instead, you can use stock images of property developments artist impression that gives a similar feel.

```html
<!DOCTYPE html>
<html lang="en">
<head>
<meta charset="utf-8">
<title>Bright Key Homes – Marketing Packages</title>
<link rel="stylesheet" href="https://fonts.googleapis.com/css2?family=Dosis:wght@400;500;600&display=swap">
<style>
  :root {
    --sky-top: #d7e6ee;
    --sky-mid: #6fa6c8;
    --globe-deep: #0e3e72;
    --panel-teal: rgba(8, 78, 104, 0.93);
    --panel-teal-solid: #0a5673;
    --accent-green: #8dc63f;
    --footer-text: #17475a;
    --white: #ffffff;
    --bubble-light: #f7f9fb;
    --bubble-dark: #93a2b0;
    --icon-blue: #3a6d98;
  }
  * { margin: 0; padding: 0; box-sizing: border-box; }
  html, body { width: 1200px; height: 835px; overflow: hidden; background: #ffffff; }
  .brochure-cover {
    position: relative;
    width: 1200px;
    height: 835px;
    overflow: hidden;
    font-family: "Dosis", sans-serif;
  }
  .cover-backdrop {
    position: absolute;
    inset: 0 0 77px 0;
    background: linear-gradient(180deg, var(--sky-top) 0%, var(--sky-mid) 42%, var(--globe-deep) 100%);
  }
  .social-nodes { position: absolute; inset: 0; }
  .headline-rule {
    position: absolute;
    left: 0; top: 158px;
    width: 652px; height: 14px;
    background: var(--accent-green);
  }
  .headline-panel {
    position: absolute;
    left: 0; top: 172px;
    width: 652px; height: 202px;
    background: var(--panel-teal);
    display: flex;
    align-items: center;
    justify-content: center;
  }
  .headline-text {
    width: 620px;
    color: var(--white);
    font-size: 25px;
    font-weight: 500;
    line-height: 32px;
    text-align: center;
    text-transform: uppercase;
  }
  .brand-rule {
    position: absolute;
    left: 746px; top: 162px;
    width: 454px; height: 14px;
    background: var(--accent-green);
  }
  .brand-panel {
    position: absolute;
    left: 746px; top: 176px;
    width: 454px; height: 204px;
    background: var(--panel-teal-solid);
    border-bottom: 5px solid var(--accent-green);
    display: flex;
    flex-direction: column;
    align-items: center;
    justify-content: center;
  }
  .brand-line { display: flex; align-items: center; gap: 12px; }
  .brand-dot {
    width: 28px; height: 28px;
    border-radius: 50%;
    background: var(--white);
  }
  .brand-name {
    color: var(--white);
    font-size: 40px;
    font-weight: 500;
    line-height: 1;
  }
  .brand-tagline {
    margin-top: 4px;
    margin-left: 40px;
    color: var(--white);
    font-size: 9px;
    font-weight: 500;
    letter-spacing: 0.6px;
    text-transform: uppercase;
  }
  .footer-band {
    position: absolute;
    left: 0; bottom: 0;
    width: 1200px; height: 77px;
    background: var(--accent-green);
    display: flex;
    align-items: center;
    justify-content: center;
  }
  .footer-url {
    color: var(--footer-text);
    font-size: 25px;
    font-weight: 500;
  }
</style>
</head>
<body>
<main class="brochure-cover">
  <div class="cover-backdrop" role="img" aria-label="City skyline of glass towers behind a glowing blue globe wrapped in network lines"></div>

  <svg class="social-nodes" width="1200" height="835" viewBox="0 0 1200 835" aria-hidden="true">
    <defs>
      <radialGradient id="bubble" cx="40%" cy="35%" r="65%">
        <stop offset="0%" stop-color="#f7f9fb"/>
        <stop offset="100%" stop-color="#93a2b0"/>
      </radialGradient>
    </defs>
    <g fill="none" stroke="#3a6d98" stroke-width="3.5" stroke-linecap="round" stroke-linejoin="round">
      <!-- envelope -->
      <circle cx="124" cy="574" r="30" fill="url(#bubble)" stroke="#7f8e9c" stroke-width="2"/>
      <rect x="110" y="565" width="28" height="19" rx="2"/>
      <polyline points="110,566 124,577 138,566"/>
      <!-- chat bubble -->
      <circle cx="344" cy="566" r="32" fill="url(#bubble)" stroke="#7f8e9c" stroke-width="2"/>
      <path d="M329 553 h30 a4 4 0 0 1 4 4 v14 a4 4 0 0 1 -4 4 h-18 l-8 7 v-7 h-4 a4 4 0 0 1 -4 -4 v-14 a4 4 0 0 1 4 -4 z"/>
      <!-- broadcast arcs -->
      <circle cx="596" cy="460" r="36" fill="url(#bubble)" stroke="#7f8e9c" stroke-width="2"/>
      <circle cx="584" cy="473" r="3" fill="#3a6d98"/>
      <path d="M582 459 a14 14 0 0 1 14 14"/>
      <path d="M582 448 a25 25 0 0 1 25 25"/>
      <!-- heart -->
      <circle cx="736" cy="554" r="36" fill="url(#bubble)" stroke="#7f8e9c" stroke-width="2"/>
      <path d="M736 570 l-14 -14 a8 8 0 0 1 14 -10 a8 8 0 0 1 14 10 z"/>
      <!-- share nodes -->
      <circle cx="932" cy="500" r="40" fill="url(#bubble)" stroke="#7f8e9c" stroke-width="2"/>
      <circle cx="920" cy="500" r="5"/>
      <circle cx="944" cy="487" r="5"/>
      <circle cx="944" cy="513" r="5"/>
      <line x1="925" y1="497" x2="939" y2="490"/>
      <line x1="925" y1="503" x2="939" y2="510"/>
      <!-- play -->
      <circle cx="1060" cy="640" r="40" fill="url(#bubble)" stroke="#7f8e9c" stroke-width="2"/>
      <polygon points="1052,626 1052,654 1074,640" fill="#3a6d98"/>
    </g>
  </svg>

  <div class="headline-rule"></div>
  <section class="headline-panel">
    <h1 class="headline-text">Get more for less – with our effective<br>marketing packages for property launches</h1>
  </section>

  <div class="brand-rule"></div>
  <section class="brand-panel">
    <div class="brand-line">
      <span class="brand-dot"></span>
      <span class="brand-name">brightkeyhomes.sg</span>
    </div>
    <span class="brand-tagline">Browse the latest property launches today!</span>
  </section>

  <footer class="footer-band">
    <span class="footer-url">www.brightkeyhomes.sg</span>
  </footer>
</main>
</body>
</html>
```